Business card design for my trucking company

I would like a business card designed for my new trucking company. Please use my logo. the rest of the design is up to you. i would like my clients to say wow when they see the card. Im looking forward to seeing your designs

Target Market(s)

Industry/Entity Type

Trucking Company

Contact Information for Business Card

Marcus Tillbrook President
518-364-7120
ridgelinehaulage@examplemail.net

Font styles to use
Serif

Requirements
Must have
• my logo, name and number. we are located in Schenectady New York. the rest is up to you
Nice to have
• up to you
Should not have
• none

```html
<!DOCTYPE html>
<html lang="en">
<head>
<meta charset="utf-8">
<title>Ridgeline Haulage &amp; Logistics – Business Card</title>
<link href="https://fonts.googleapis.com/css2?family=Lora:wght@400;700&display=swap" rel="stylesheet">
<style>
  :root {
    --bg: #2a2a2c;
    --card: #ffffff;
    --red: #e41e26;
    --grey: #6d6e71;
    --ink: #58595b;
    --map: #ececec;
    --rule: #9a9a9a;
  }
  * { box-sizing: border-box; margin: 0; padding: 0; }
  html, body { width: 1200px; height: 900px; overflow: hidden; }
  body {
    background: var(--bg);
    font-family: "Lora", serif;
    position: relative;
  }
  .card {
    position: absolute;
    left: 280px;
    width: 640px;
    height: 366px;
    background: var(--card);
    border-radius: 22px;
    overflow: hidden;
  }
  .card--front { top: 64px; }
  .card--back { top: 470px; }

  .map-area {
    position: absolute;
    left: 50px; top: 40px;
    width: 540px; height: 286px;
    border-radius: 40px;
    background: radial-gradient(ellipse at center, var(--map) 0%, #f5f5f5 60%, rgba(255,255,255,0) 100%);
  }
  .brand {
    position: absolute;
    display: flex;
    align-items: center;
    gap: 12px;
  }
  .brand__mark {
    width: 20px; height: 20px;
    border-radius: 50%;
    background: var(--red);
    flex: none;
  }
  .brand__name {
    font-weight: 700;
    color: var(--red);
    text-transform: uppercase;
    line-height: 1.15;
    letter-spacing: 0.5px;
    white-space: nowrap;
  }
  .card--front .brand { left: 0; right: 0; top: 0; bottom: 0; justify-content: center; }
  .card--front .brand__name { font-size: 30px; }
  .card--back .brand { left: 34px; top: 148px; }
  .card--back .brand__name { font-size: 17px; }

  .divider {
    position: absolute;
    left: 318px; top: 82px;
    width: 1px; height: 170px;
    background: var(--rule);
  }
  .contact {
    position: absolute;
    left: 338px; top: 76px;
    color: var(--ink);
  }
  .contact__name { color: var(--red); font-weight: 700; font-size: 23px; line-height: 1.15; }
  .contact__title { font-size: 14px; margin-bottom: 10px; }
  .contact__address { font-size: 13px; line-height: 1.4; margin-bottom: 10px; }
  .contact__list { list-style: none; font-size: 12.5px; line-height: 1.6; }
  .contact__list li { display: flex; align-items: center; gap: 8px; }
  .contact__list svg { width: 11px; height: 11px; flex: none; }
  .edge-band { position: absolute; left: 0; bottom: 0; width: 640px; height: 18px; }
</style>
</head>
<body>
  <section class="card card--front">
    <div class="map-area" role="img" aria-label="Faint dotted world map behind the company name"></div>
    <div class="brand">
      <span class="brand__mark"></span>
      <span class="brand__name">Ridgeline Haulage<br>&amp; Logistics Inc.</span>
    </div>
  </section>

  <section class="card card--back">
    <div class="brand">
      <span class="brand__mark"></span>
      <span class="brand__name">Ridgeline Haulage<br>&amp; Logistics Inc.</span>
    </div>
    <div class="divider"></div>
    <div class="contact">
      <p class="contact__name">Marcus Tillbrook</p>
      <p class="contact__title">President</p>
      <p class="contact__address">1450 Erie Boulevard<br>Schenectady, NY 12305</p>
      <ul class="contact__list">
        <li>
          <svg viewBox="0 0 12 12"><path fill="#e41e26" d="M2.5 1 L4.5 1 L5.2 3.5 L4 4.6 C4.7 6 6 7.3 7.4 8 L8.5 6.8 L11 7.5 L11 9.5 C11 10.3 10.3 11 9.5 11 C5 11 1 7 1 2.5 C1 1.7 1.7 1 2.5 1 Z"/></svg>
          518-364-7120
        </li>
        <li>
          <svg viewBox="0 0 12 12"><rect x="0.5" y="2" width="11" height="8" fill="#e41e26"/><path d="M0.5 2 L6 6.5 L11.5 2" fill="none" stroke="#fff" stroke-width="1"/></svg>
          ridgelinehaulage@examplemail.net
        </li>
        <li>
          <svg viewBox="0 0 12 12"><circle cx="6" cy="6" r="5.5" fill="#e41e26"/><path d="M0.5 6 H11.5 M6 0.5 C3.5 3 3.5 9 6 11.5 M6 0.5 C8.5 3 8.5 9 6 11.5" fill="none" stroke="#fff" stroke-width="0.8"/></svg>
          www.ridgelinehaulage.com
        </li>
      </ul>
    </div>
    <svg class="edge-band" viewBox="0 0 640 18" preserveAspectRatio="none" aria-hidden="true">
      <polygon points="0,12 404,12 410,18 0,18" fill="#e41e26"/>
      <polygon points="398,0 640,0 640,18 414,18" fill="#6d6e71"/>
    </svg>
  </section>
</body>
</html>
```